Business Card Design

We have a group of different function companies owned and operated by one person. We are located in the Dallas Fort Worth area in Texas. We develop properties to where we are owners and develop properties that are not ours as well. We build custom homes and commercial buildings. We also do residential and commercial remodeling. We also own commercial properties in which we lease office space. We are trying to merge all we do into one card and have done so already into one website. We initially had thought of having a logo made with HV in nice attractive lettering maybe as a watermark. We are open to the color scheme but no neons or pastels.

Project Deadline Extended
Reason: I am needing 2 different cards for two businesses.

Industry/Entity Type

Residential

Contact Information for Business Card

Harwell Ventures
4826 Mabry Ln. Suite 417
Keller, Texas 76109
Land Development
Residential and Commercial Construction
Commercial Real Estate
Dale Wintermoot
www.harwellgrp.example
dale@harwellgrp.example
Cell: 817-555-0142
Office: 817-555-0187
Fax: 8175550163

```html
<!DOCTYPE html>
<html lang="en">
<head>
<meta charset="utf-8">
<title>Harwell Ventures – Business Card</title>
<link rel="stylesheet" href="https://fonts.googleapis.com/css2?family=Alegreya:ital,wght@0,400;0,700;1,400&family=Bree+Serif&display=swap">
<style>
  :root {
    --backdrop: #e8e3db;
    --card-white: #fbfbfb;
    --pattern-light: #f4f4f4;
    --pattern-mid: #e2e2e2;
    --ink-brown: #6a3a1c;
    --ink-dark: #1c1c1c;
    --band-tagline: #c98a3f;
    --tagline-text: #7b4520;
    --band-main: #a95f24;
    --band-base: #8c5128;
    --web-text: #d2a67c;
    --white: #ffffff;
  }
  html, body {
    margin: 0;
    width: 1200px;
    height: 1000px;
    overflow: hidden;
    background: var(--backdrop);
  }
  .card {
    position: absolute;
    left: 100px;
    top: 214px;
    width: 1000px;
    height: 571px;
    background: var(--card-white);
    box-shadow: 0 4px 18px rgba(0,0,0,0.18);
    overflow: hidden;
    font-family: "Alegreya", Georgia, serif;
  }
  .card__pattern {
    position: absolute;
    inset: 0 0 206px 0;
    background: linear-gradient(135deg, var(--pattern-light) 0%, var(--card-white) 40%, var(--pattern-mid) 70%, var(--pattern-light) 100%);
    opacity: 0.7;
  }
  .brand-name {
    position: absolute;
    right: 60px;
    top: 58px;
    margin: 0;
    font-size: 38px;
    font-weight: 400;
    letter-spacing: 3px;
    text-transform: uppercase;
    color: var(--ink-dark);
  }
  .person {
    position: absolute;
    left: 70px;
    top: 200px;
    color: var(--ink-brown);
  }
  .person__name {
    margin: 0;
    font-family: "Bree Serif", Georgia, serif;
    font-size: 46px;
    font-weight: 400;
    line-height: 1.1;
  }
  .person__title {
    margin: 4px 0 0 14px;
    font-size: 42px;
    line-height: 1.1;
  }
  .person__email {
    margin: 14px 0 0 28px;
    font-size: 38px;
    font-style: italic;
    line-height: 1.1;
  }
  .band {
    position: absolute;
    left: 0;
    right: 0;
  }
  .band--tagline {
    top: 365px;
    height: 36px;
    background: var(--band-tagline);
    color: var(--tagline-text);
    font-size: 23px;
    line-height: 36px;
    text-align: center;
    white-space: nowrap;
  }
  .band--main {
    top: 401px;
    height: 105px;
    background: var(--band-main);
  }
  .band--base {
    top: 506px;
    height: 65px;
    background: var(--band-base);
  }
  .contact {
    position: absolute;
    right: 50px;
    margin: 0;
    color: var(--white);
    font-size: 31px;
    white-space: nowrap;
    text-align: right;
  }
  .contact--address { top: 418px; }
  .contact--phones { top: 468px; }
  .website {
    position: absolute;
    left: 0;
    right: 0;
    top: 520px;
    margin: 0;
    text-align: center;
    color: var(--web-text);
    font-size: 26px;
    letter-spacing: 6px;
  }
</style>
</head>
<body>
  <section class="card">
    <div class="card__pattern" role="img" aria-label="Soft light grey diagonal pattern background"></div>

    <h1 class="brand-name">Harwell Ventures</h1>

    <div class="person">
      <h2 class="person__name">Dale Wintermoot</h2>
      <p class="person__title">President</p>
      <p class="person__email">dale@harwellgrp.example</p>
    </div>

    <div class="band band--tagline">Land Development Residential and Commercial Construction Commercial Real Estate</div>
    <div class="band band--main"></div>
    <div class="band band--base"></div>

    <p class="contact contact--address">4826 Mabry Ln. Suite 417&nbsp; / &nbsp;Keller, Texas 76109</p>
    <p class="contact contact--phones">Cell: 817-555-0142&nbsp; / &nbsp;Office: 817-555-0187&nbsp; / &nbsp;Fax: 817-555-0163</p>
    <p class="website">www.harwellgrp.example</p>
  </section>
</body>
</html>
```